KGDB Business Card

Looking for a business card design to incorporate our branding. We want to only use the colors listing in the Branding Package (attached).
Updates

Target Market(s)

People who need their phone or device fixed.

Industry/Entity Type

Electronics

Contact Information for Business Card

Please use:

Bright Circuit Mending Depot LLC
3478 S Ridge Trail 2210 E
Suite 417
San Antonio, TX 78341

Marcus Delwyn, Store Manager

(210) 555-0143

Requirements
Must have
• Must include the colors that are contained within the Branding Package PDF file.

```html
<!DOCTYPE html>
<html lang="en">
<head>
<meta charset="utf-8">
<title>KGDB Business Card</title>
<link href="https://fonts.googleapis.com/css2?family=Source+Sans+3:wght@400;600;700&display=swap" rel="stylesheet">
<style>
  :root {
    --orange: #e0582c;
    --orange-dark: #a8401f;
    --peach: #f6d6c3;
    --peach-mid: #eeb896;
    --blush: #f1c7b4;
    --white: #ffffff;
    --ink: #4a2a1e;
    --backdrop: #c4c4c8;
  }
  html, body {
    margin: 0;
    width: 1200px;
    height: 1200px;
    overflow: hidden;
    background: var(--backdrop);
    font-family: "Source Sans 3", sans-serif;
  }
  .canvas {
    position: relative;
    width: 1200px;
    height: 1200px;
  }
  .card {
    position: absolute;
    top: 210px;
    width: 400px;
    height: 780px;
    border-radius: 64px;
    box-sizing: border-box;
    border: 5px solid var(--orange);
    overflow: hidden;
  }
  /* Front */
  .card-front {
    left: 140px;
    background: linear-gradient(180deg, var(--white) 0%, var(--white) 60%, #f8e2d4 100%);
  }
  .earpiece {
    position: absolute; top: 52px; left: 160px;
    width: 70px; height: 8px; border-radius: 4px; background: var(--orange);
  }
  .sensor {
    position: absolute; top: 34px; left: 193px;
    width: 11px; height: 11px; border-radius: 50%; background: var(--orange);
  }
  .front-camera {
    position: absolute; top: 50px; left: 118px;
    width: 12px; height: 12px; border-radius: 50%; background: var(--orange-dark);
  }
  .screen {
    position: absolute; top: 92px; left: 28px; right: 28px; bottom: 120px;
    background: linear-gradient(180deg, #fbeee6, #f6ddcf);
  }
  .status-bar {
    height: 24px; background: var(--orange); color: var(--white);
    display: flex; align-items: center; justify-content: space-between;
    padding: 0 10px; font-size: 11px; font-weight: 700;
  }
  .profile {
    display: flex; align-items: center; gap: 16px;
    padding: 12px 16px; background: var(--blush);
  }
  .avatar {
    width: 64px; height: 64px; border-radius: 50%;
    background: radial-gradient(circle at 50% 40%, #b85530, var(--orange-dark));
    border: 3px solid var(--white);
    flex: none;
  }
  .name {
    margin: 0; font-size: 19px; font-weight: 700; color: var(--ink); letter-spacing: 0.5px;
  }
  .title { margin: 2px 0 0; font-size: 14px; color: var(--ink); }
  .row {
    position: relative; display: flex; align-items: center; gap: 12px;
    padding: 16px 40px 16px 18px;
    border-bottom: 1px solid #ecc6b2;
    background: linear-gradient(90deg, var(--white), #f8e6dc);
    color: var(--ink);
  }
  .row-company { font-size: 17px; font-weight: 600; line-height: 1.5; letter-spacing: 0.4px; text-transform: uppercase; }
  .row-phone { font-size: 17px; }
  .row-address { font-size: 14px; line-height: 1.35; }
  .chevron {
    position: absolute; right: 12px; top: 14px;
    width: 16px; height: 16px;
  }
  .row-icon { width: 22px; height: 22px; flex: none; }
  .unlock-panel {
    padding: 20px 16px; background: linear-gradient(180deg, #f3cdb9, #eebba0);
  }
  .unlock-track {
    display: flex; align-items: center; gap: 20px;
    border: 2px solid var(--orange); border-radius: 8px;
    padding: 6px; background: rgba(255,255,255,0.35);
  }
  .unlock-knob {
    width: 64px; height: 40px; border-radius: 6px; background: var(--orange);
    display: flex; align-items: center; justify-content: center;
  }
  .unlock-label { font-size: 24px; color: var(--orange-dark); }
  .call-band {
    position: absolute; left: 0; right: 0; bottom: 0; height: 60px;
    background: var(--peach-mid); display: flex; align-items: center; justify-content: center;
  }
  .call-button {
    width: 260px; height: 38px; border-radius: 19px; background: var(--white);
    display: flex; align-items: center; justify-content: center; gap: 40px;
    color: var(--orange); font-weight: 700; font-size: 16px;
  }
  .home-button {
    position: absolute; bottom: 34px; left: 167px;
    width: 56px; height: 56px; border-radius: 50%;
    border: 3px solid var(--orange); background: var(--white); box-sizing: border-box;
  }
  /* Back */
  .card-back {
    left: 660px;
    background: linear-gradient(180deg, #f6d3bc 0%, #eca57d 60%, var(--orange) 100%);
  }
  .rear-camera {
    position: absolute; top: 60px; left: 44px;
    width: 40px; height: 40px; border-radius: 50%;
    background: #3a3a3e; border: 4px solid #8a8a8e; box-sizing: border-box;
  }
  .rear-flash {
    position: absolute; top: 68px; left: 100px;
    width: 22px; height: 22px; border-radius: 50%; background: #9a9a9c;
  }
  .brand {
    position: absolute; left: 60px; bottom: 150px;
    display: flex; align-items: center; gap: 16px;
  }
  .brand-square {
    width: 50px; height: 50px; border-radius: 8px; background: var(--white);
  }
  .brand-name {
    font-size: 54px; font-weight: 600; color: var(--white); letter-spacing: 2px;
  }
</style>
</head>
<body>
<main class="canvas">

  <section class="card card-front">
    <div class="sensor"></div>
    <div class="front-camera"></div>
    <div class="earpiece"></div>

    <div class="screen">
      <div class="status-bar">
        <span>Volt 3G</span><span>9:41 AM</span><span>100%</span>
      </div>

      <div class="profile">
        <div class="avatar" role="img" aria-label="Staff portrait placeholder"></div>
        <div>
          <p class="name">MARCUS DELWYN</p>
          <p class="title">Store Manager</p>
        </div>
      </div>

      <div class="row row-company">
        Bright Circuit Mending<br>Depot LLC
        <svg class="chevron" viewBox="0 0 16 16"><circle cx="8" cy="8" r="8" fill="var(--orange)"/><path d="M6.5 4.5 10 8l-3.5 3.5" stroke="#fff" stroke-width="2" fill="none"/></svg>
      </div>

      <div class="row row-phone">
        <svg class="row-icon" viewBox="0 0 24 24"><path d="M6 3h4l2 5-3 2a12 12 0 0 0 5 5l2-3 5 2v4a2 2 0 0 1-2 2A17 17 0 0 1 4 5a2 2 0 0 1 2-2z" fill="var(--orange)"/></svg>
        (210) 555-0143
        <svg class="chevron" viewBox="0 0 16 16"><circle cx="8" cy="8" r="8" fill="var(--orange)"/><path d="M6.5 4.5 10 8l-3.5 3.5" stroke="#fff" stroke-width="2" fill="none"/></svg>
      </div>

      <div class="row row-address">
        <svg class="row-icon" viewBox="0 0 24 24"><path d="M12 2a7 7 0 0 0-7 7c0 5 7 13 7 13s7-8 7-13a7 7 0 0 0-7-7zm0 9.5A2.5 2.5 0 1 1 12 6.5a2.5 2.5 0 0 1 0 5z" fill="var(--orange)"/></svg>
        <span>3478 S Ridge Trail 2210 E<br>Suite 417<br>San Antonio, TX 78341</span>
        <svg class="chevron" viewBox="0 0 16 16"><circle cx="8" cy="8" r="8" fill="var(--orange)"/><path d="M6.5 4.5 10 8l-3.5 3.5" stroke="#fff" stroke-width="2" fill="none"/></svg>
      </div>

      <div class="unlock-panel">
        <div class="unlock-track">
          <div class="unlock-knob">
            <svg width="30" height="22" viewBox="0 0 30 22"><path d="M2 8h14V2l12 9-12 9v-6H2z" fill="#fff"/></svg>
          </div>
          <span class="unlock-label">slide to unlock</span>
        </div>
      </div>

      <div class="call-band">
        <div class="call-button">
          <svg width="16" height="18" viewBox="0 0 24 24"><path d="M6 3h4l2 5-3 2a12 12 0 0 0 5 5l2-3 5 2v4a2 2 0 0 1-2 2A17 17 0 0 1 4 5a2 2 0 0 1 2-2z" fill="var(--orange-dark)"/></svg>
          <span>Call</span>
        </div>
      </div>
    </div>

    <div class="home-button"></div>
  </section>

  <section class="card card-back">
    <div class="rear-camera"></div>
    <div class="rear-flash"></div>
    <div class="brand">
      <div class="brand-square"></div>
      <span class="brand-name">KGDB</span>
    </div>
  </section>

</main>
</body>
</html>
```